Single-sided business card for restaurant bellwether with new logo made on this site

Business card options with new logo including restaurant name, address, phone number and website. This business card is single-sided only and will be presented at the hostess desk for clients to take. I would like to see options based on a cream card background, a white card background, a yellow card background and a burgundy colored background. It needs to be elegant and traditional.

Target Market(s)

local and international crowd

Industry/Entity Type

restaurant

Contact Information for Business Card

address, website and phone number

Font styles to use
Serif

Colors
EE7325
F08F49
F5BC92
FAE3D3
FDF4ED

Requirements
Must have
• new logo, address, phone number, website
Should not have
• more than three colors

```html
<!DOCTYPE html>
<html lang="es">
<head>
<meta charset="utf-8">
<title>Bellwether Restaurant – Business Card</title>
<link rel="stylesheet" href="https://fonts.googleapis.com/css2?family=Cinzel:wght@600&family=Gelasio:wght@400&family=Montserrat:wght@400&display=swap">
<style>
  :root{
    --burgundy:#3f1c1e;
    --gold:#f5b22c;
    --gold-text:#f4ab1e;
    --paper:#fbfaf8;
    --ink:#2b2b2b;
    --stage:#ffffff;
    --leaf-tint:#f7ecd6;
  }
  *{box-sizing:border-box;margin:0;padding:0}
  html,body{width:887px;height:1200px;overflow:hidden;background:var(--stage)}
  .canvas{position:relative;width:887px;height:1200px}
  .card{
    position:absolute;left:44px;top:372px;width:800px;height:457px;
    background:var(--paper);overflow:hidden;
    box-shadow:0 6px 22px rgba(60,70,80,.22);
  }
  .brand-panel{position:absolute;left:0;top:0;width:348px;height:457px;background:var(--burgundy)}
  .brand-frame{
    position:absolute;left:26px;top:28px;width:274px;height:401px;background:var(--gold);
    display:flex;flex-direction:column;align-items:center;justify-content:center;gap:30px;
    padding:0 24px;
  }
  .brand-frame::after{
    content:"";position:absolute;inset:10px;border:4px solid var(--burgundy);
  }
  .brand-mark{width:70px;height:70px;border-radius:50%;background:var(--burgundy)}
  .brand-name{
    font-family:"Cinzel",serif;font-weight:600;font-size:26px;letter-spacing:2px;
    color:var(--burgundy);line-height:1;white-space:nowrap;
  }
  .leaf-wash{
    position:absolute;left:430px;top:90px;width:370px;height:367px;
    background:radial-gradient(ellipse at 60% 75%,var(--leaf-tint) 0%,rgba(247,236,214,.5) 45%,rgba(251,250,248,0) 75%);
  }
  .icon-rail{
    position:absolute;left:327px;top:68px;width:38px;height:311px;
    background:var(--gold);border-radius:4px;
  }
  .icon-rail svg{position:absolute;left:9px;width:21px;height:21px;fill:none;stroke:#fff;stroke-width:2}
  .icon-phone{top:86px}
  .icon-pin{top:164px}
  .icon-globe{top:262px}
  .details{position:absolute;left:388px;top:60px;color:var(--ink);font-family:"Gelasio",serif}
  .name{font-family:"Cinzel",serif;font-weight:600;font-size:31px;letter-spacing:2px;color:var(--gold-text);line-height:1}
  .tagline{font-family:"Montserrat",sans-serif;font-size:20px;letter-spacing:1px;color:#333;margin-top:2px}
  .reserve{margin-top:26px;font-size:20px;line-height:1}
  .phone{font-size:27px;letter-spacing:1px;line-height:1.05}
  .address{margin-top:20px;font-size:20px;line-height:1.3}
  .web{margin-top:27px;font-size:19px;letter-spacing:.5px}
</style>
</head>
<body>
<main class="canvas">
  <article class="card">
    <section class="brand-panel">
      <div class="brand-frame">
        <span class="brand-mark" aria-hidden="true"></span>
        <span class="brand-name">BELLWETHER</span>
      </div>
    </section>

    <div class="leaf-wash" role="img" aria-label="Faint pale agave leaves decoration"></div>

    <div class="icon-rail" aria-hidden="true">
      <svg class="icon-phone" viewBox="0 0 24 24"><path d="M5 3h4l2 5-2.5 1.5a11 11 0 0 0 6 6L16 13l5 2v4a2 2 0 0 1-2 2A16 16 0 0 1 3 5a2 2 0 0 1 2-2z"/><path d="M15 3a6 6 0 0 1 6 6M15 7a2 2 0 0 1 2 2"/></svg>
      <svg class="icon-pin" viewBox="0 0 24 24"><path d="M12 21s-6-6-6-11a6 6 0 0 1 12 0c0 5-6 11-6 11z"/><circle cx="12" cy="10" r="2.2"/><path d="M5 20h14"/></svg>
      <svg class="icon-globe" viewBox="0 0 24 24"><circle cx="12" cy="12" r="9"/><path d="M3 12h18M12 3c3 3 3 15 0 18M12 3c-3 3-3 15 0 18M5 7h14M5 17h14"/></svg>
    </div>

    <section class="details">
      <h1 class="name">BELLWETHER</h1>
      <p class="tagline">RESTAURANT</p>
      <p class="reserve">Reservaciones</p>
      <p class="phone">958-214-3078</p>
      <p class="address">Jacarandá 417<br>Santa María del Mar, Oaxaca<br>CP 70412</p>
      <p class="web">www.bellwether.com.mx</p>
    </section>
  </article>
</main>
</body>
</html>
```